Business Card for KRB Farmhaul

Custom Business Card Brief:
1. We need two designs for this single client, KRB Farmhaul LLC and both designs will end up with rounded corner printed cards that fit the ZIVA.com design format for their special printing style.
2. My client needs two separate card designs since half of their target market is for farm owners in the Cattle and Beef world. The other half of their target market is working with Equine aka Horse farm owners.
3. The look for two card designs can be similar to ensure branding consistency but we will need some space sizing differences so the cards stand out differently in regards to how the services mentioned are laid out on the front of each card design.
4. Both card designs require the front of the card holding all of the great design work. The back of these 2-sided cards will remain white and can just have the contact information listed "again" on the back to match the contact information provided on the front.
5. Card Design 1 will be for Equine customers, Card Design 2 will be for his Cattle/Beef customers.
6. Card Design 1 (Equine) we are thinking we set aside 70% of the card to be dedicated to the Services listed section while the remaining 30% of the front of the card space will hold a smaller logo image space along with his name and contact information.
7. Card Design 2 (Cattle/Beef) we will need opposite of my last point. We want 70% of the card dedicated to a larger logo space and his contact information while the remaining 30% listing the services provided.
8. Card Design #1 - Equine - his Services space should include:
- Equine Mortality Services
- General Removal
- Cremation
- Transportation for Necropsy
9. Card Design #2 - Cattle/Beef - his Services space should include: General Livestock Services, Hauling, Order Buying, Dealing, Dead Stock Removal
10. Contact Information for both card designs:
- Dennis R. Hollorand (owner)
- KRB Farmhaul LLC (company)
- 608-413-5972 (phone)
- info@krbfarmhaulgroup.example (email)
- KRBFarmhaulGroup.example (website)
11. Additional Branding Details - The color codes aka pantone colors that are in the current logo file design:
- Blue Pantone 7686C
- Grey Pantone 422C
12. The font styles used in the logo:
- Nexa Bold
- Nexa Rust Slab Black Shadow
13. Back of both card designs, just list his contact information in larger size to stand out more on the white back:
- 608-413-5972 (phone)
Updates

Okay thanks for confirming that our final design files will be ready for the ZIVA.com format. I noticed the 2nd place vertical card already had rounded corners but the horizontal design that was in 1st place still had sharp square corners. When using the ZIVA.com format we will be rounding all of the corners of both cards for print. So we just wanted to make sure that both sets of files will be in a rounded design meeting their format sizing to ensure no content from your great designs gets cut off. Thank you again for your attention to detail. ~ Glenn

Target Market(s)

Business to Business

Industry/Entity Type

Farming, Agriculture, Livestock

Contact Information for Business Card

Clients' logo, his contact info, and his different services on two similar final card designs.

Font styles to use
Other font styles liked:
• Look at the brief to see how his logo fonts are currently.

Requirements
Must have
• Two versions of the card, one for the Equine horse market, and one for the Cattle/Beef market of farming.
Nice to have
• Clean, sharp, concise.
Should not have
• No flashy or cartoony designs.

```html
<!DOCTYPE html>
<html lang="en">
<head>
<meta charset="utf-8">
<title>KRB Farmhaul – Business Card</title>
<link href="https://fonts.googleapis.com/css2?family=Lexend:wght@400;500;600&display=swap" rel="stylesheet">
<style>
  :root {
    --page-bg: #e8eced;
    --card-bg: #ffffff;
    --brand-green: #177862;
    --brand-text: #177a64;
    --accent-mint: #3ee0a8;
    --on-green: #ffffff;
    --card-shadow: rgba(0, 0, 0, 0.5);
  }
  * { margin: 0; padding: 0; box-sizing: border-box; }
  html, body {
    width: 1197px; height: 1200px; overflow: hidden;
    background: var(--page-bg);
    font-family: "Lexend", "Helvetica Neue", Arial, sans-serif;
  }
  .stage { position: relative; width: 1197px; height: 1200px; }

  .card {
    position: absolute; left: 203px; width: 790px;
    background: var(--card-bg);
    box-shadow: 9px 9px 6px var(--card-shadow);
    overflow: hidden;
  }
  .card--front { top: 110px; height: 451px; border-radius: 20px; }
  .card--back { top: 672px; height: 417px; border-radius: 20px 20px 0 0; }

  .front-panel { position: absolute; inset: 0; width: 100%; height: 100%; }

  .wordmark {
    position: absolute; font-weight: 600; letter-spacing: 0.06em; white-space: nowrap;
  }
  .card--front .wordmark { left: 30px; top: 76px; font-size: 24px; color: var(--on-green); }
  .card--back .wordmark {
    left: 214px; top: 226px; transform: translate(-50%, -50%);
    font-size: 40px; color: var(--brand-text);
  }

  .holder { position: absolute; letter-spacing: 0.1em; font-weight: 500; }
  .card--front .holder { left: 30px; top: 264px; color: var(--on-green); }
  .card--front .holder-name { font-size: 16.5px; }
  .card--front .holder-role { font-size: 12px; margin-top: 7px; }
  .card--back .holder { left: 409px; top: 107px; color: var(--brand-text); }
  .card--back .holder-name { font-size: 24px; font-weight: 600; }
  .card--back .holder-role { font-size: 18px; font-weight: 600; line-height: 1; }

  .contact-list { position: absolute; list-style: none; letter-spacing: 0.08em; }
  .contact-list li { display: flex; align-items: center; white-space: nowrap; }
  .contact-list svg { flex: none; fill: none; stroke: currentColor; stroke-width: 1.3; }
  .card--front .contact-list { left: 28px; top: 350px; color: var(--on-green); font-size: 12.5px; }
  .card--front .contact-list li { height: 26px; gap: 12px; }
  .card--front .contact-list svg { width: 14px; height: 14px; }
  .card--back .contact-list { left: 417px; top: 222px; color: var(--brand-text); font-size: 16px; font-weight: 500; }
  .card--back .contact-list li { height: 48.5px; gap: 16px; }
  .card--back .contact-list svg { width: 18px; height: 18px; }

  .services { position: absolute; left: 340px; top: 128px; color: var(--brand-text); }
  .services-title { font-size: 28px; font-weight: 600; letter-spacing: 0.08em; margin-bottom: 14px; }
  .service-list { list-style: none; }
  .service-list li {
    display: flex; align-items: center; gap: 14px; height: 39.5px;
    font-size: 19px; letter-spacing: 0.1em; white-space: nowrap;
  }
  .service-list svg { width: 29px; height: 27px; fill: var(--brand-text); flex: none; }

  .divider {
    position: absolute; left: 380px; top: 87px; width: 2px; height: 277px;
    background: var(--brand-green);
  }
</style>
</head>
<body>
<main class="stage">

  <section class="card card--front" aria-label="Card front">
    <svg class="front-panel" viewBox="0 0 790 451" preserveAspectRatio="none" aria-hidden="true">
      <polygon points="196,0 353,451 346,451 189,0" fill="var(--accent-mint)"/>
      <polygon points="0,0 189,0 346,451 0,451" fill="var(--brand-green)"/>
    </svg>

    <div class="wordmark">KRB Farmhaul</div>

    <div class="holder">
      <div class="holder-name">Dennis R. Hollorand</div>
      <div class="holder-role">Owner</div>
    </div>

    <ul class="contact-list">
      <li>
        <svg viewBox="0 0 16 16"><path d="M3 2l3 0 1 3-2 1.5c1 2 2.5 3.5 4.5 4.5L11 9l3 1v3c-6 1-12-5-11-11z"/><path d="M10 2a4 4 0 0 1 4 4M10 4.5a1.6 1.6 0 0 1 1.5 1.5"/></svg>
        608-413-5972
      </li>
      <li>
        <svg viewBox="0 0 16 16"><rect x="1.5" y="3.5" width="13" height="9"/><path d="M1.5 3.5l6.5 5 6.5-5M1.5 12.5l5-4.5M14.5 12.5l-5-4.5"/></svg>
        info@krbfarmhaulgroup.example
      </li>
      <li>
        <svg viewBox="0 0 16 16"><circle cx="8" cy="8" r="6.5"/><ellipse cx="8" cy="8" rx="3" ry="6.5"/><path d="M1.5 8h13M2.5 4.8h11M2.5 11.2h11"/></svg>
        KRBFarmhaulGroup.example
      </li>
    </ul>

    <div class="services">
      <h2 class="services-title">Services</h2>
      <ul class="service-list">
        <li><svg viewBox="0 0 29 27"><path d="M1 15l5-4 5 6L25 1l3 3L11 26z"/></svg>Equine Mortality Services</li>
        <li><svg viewBox="0 0 29 27"><path d="M1 15l5-4 5 6L25 1l3 3L11 26z"/></svg>General Removal</li>
        <li><svg viewBox="0 0 29 27"><path d="M1 15l5-4 5 6L25 1l3 3L11 26z"/></svg>Cremation</li>
        <li><svg viewBox="0 0 29 27"><path d="M1 15l5-4 5 6L25 1l3 3L11 26z"/></svg>Transportation For Necropsy</li>
      </ul>
    </div>
  </section>

  <section class="card card--back" aria-label="Card back">
    <div class="wordmark">KRB Farmhaul</div>
    <div class="divider"></div>

    <div class="holder">
      <div class="holder-name">Dennis R. Hollorand</div>
      <div class="holder-role">Owner</div>
    </div>

    <ul class="contact-list">
      <li>
        <svg viewBox="0 0 16 16"><path d="M3 2l3 0 1 3-2 1.5c1 2 2.5 3.5 4.5 4.5L11 9l3 1v3c-6 1-12-5-11-11z"/><path d="M10 2a4 4 0 0 1 4 4M10 4.5a1.6 1.6 0 0 1 1.5 1.5"/></svg>
        608-413-5972
      </li>
      <li>
        <svg viewBox="0 0 16 16"><rect x="1.5" y="3.5" width="13" height="9"/><path d="M1.5 3.5l6.5 5 6.5-5M1.5 12.5l5-4.5M14.5 12.5l-5-4.5"/></svg>
        info@krbfarmhaulgroup.example
      </li>
      <li>
        <svg viewBox="0 0 16 16"><circle cx="8" cy="8" r="6.5"/><ellipse cx="8" cy="8" rx="3" ry="6.5"/><path d="M1.5 8h13M2.5 4.8h11M2.5 11.2h11"/></svg>
        KRBFarmhaulGroup.example
      </li>
    </ul>
  </section>

</main>
</body>
</html>
```